Outdoor sign for Brindle Auto Restoration

I need a horizontal 4'x 8' outdoor roadside sign for my classic auto restoration business. I have uploaded colors and our logo. Needs the Brindle name, a prominent Classic AUTO RESTORATION, phone number and website. We rebuild and restore vintage cars, trucks and 4x4s. I'd like something clean but possibly retro. Classic Auto Restoration is more important than the Brindle name. It needs to be visible and readable from the street. NO CLIP ART

Target Market(s)

Customers who need their vintage care restored or upgraded. Men and women ages 25-75

Industry/Entity Type

Automotive

Colors
FFC000
F8CF3A
FAE287
FDF2CF
FEFAEE

Requirements
Must have
• Legible. Bright. Readable as a backlit 4' x 8' large horizontal sign (roughly 120cm X 240cm)
Nice to have
• Use of the Brindle logo/type, Complete or Classic before prominent AUTO RESTORATION
Should not have
• Clip art of old cars or icons. And we don't want the Brindle Logo from the website because it wont be legible from the road. I have included the Illustrator file for Brindle text in the uploads

```html
<!DOCTYPE html>
<html lang="en">
<head>
<meta charset="UTF-8">
<title>Brindle Auto Restoration – Roadside Sign</title>
<link rel="stylesheet" href="https://fonts.googleapis.com/css2?family=Michroma&family=Roboto:wght@900&display=swap">
<style>
  :root {
    --sign-black: #0c0d0c;
    --sign-gold: #f5ae1f;
    --sign-white: #ffffff;
    --page: #ffffff;
  }
  html, body {
    margin: 0;
    padding: 0;
    width: 864px;
    height: 1200px;
    overflow: hidden;
    background: var(--page);
  }
  .canvas {
    position: relative;
    width: 864px;
    height: 1200px;
  }
  .roadside-sign {
    position: absolute;
    left: 36px;
    top: 402px;
    width: 792px;
    height: 396px;
    display: block;
  }
  .sign-panel { fill: var(--sign-black); }
  .tagline-band { fill: var(--sign-gold); }
  .business-name {
    font-family: "Roboto", "Arial", sans-serif;
    font-weight: 900;
    fill: var(--sign-gold);
  }
  .service-line {
    font-family: "Michroma", "Arial", sans-serif;
    fill: var(--sign-black);
    stroke: var(--sign-black);
    stroke-width: 1.5;
  }
  .contact-line {
    font-family: "Roboto", "Arial", sans-serif;
    font-weight: 900;
    fill: var(--sign-white);
  }
  .contact-dot { fill: var(--sign-gold); }
</style>
</head>
<body>
<main class="canvas">
  <svg class="roadside-sign" viewBox="0 0 1513 756" role="img" aria-label="Brindle Auto Restoration sign">
    <rect class="sign-panel" x="0" y="0" width="1513" height="756"/>

    <text class="business-name" x="226" y="340" font-size="210" textLength="1061" lengthAdjust="spacingAndGlyphs">BRINDLE</text>

    <rect class="tagline-band" x="117" y="404" width="1279" height="111"/>
    <text class="service-line" x="319" y="479" font-size="54" textLength="865" lengthAdjust="spacingAndGlyphs">AUTO RESTORATION</text>

    <text class="contact-line contact-phone" x="340" y="600" font-size="44" textLength="260" lengthAdjust="spacingAndGlyphs">501-555-0142</text>
    <circle class="contact-dot" cx="648" cy="586" r="8"/>
    <text class="contact-line contact-web" x="695" y="600" font-size="44" textLength="478" lengthAdjust="spacingAndGlyphs">brindle autoworks.com</text>
  </svg>
</main>
</body>
</html>
```